PawCrate Banner contest an ecommerce site for veterinarians

We need banners for our ecommerce site. Our site is a webstore that veterinarians can use to allow their clients to purchase items from them. Each month we have a different theme for our banners. I am looking for banners for January and February and with a refresh coming to our site could be looking at a dozen over the next year. I may potentially choose from multiple designers and increase the payment or will choose one designer for both months .

For January our theme is winter fun. We will be running a contest were people can submit a picture of their pet to our Chirpbook page enjoying the snow or keeping warm. they have a chance to win one of 5 $50 gift certificates to pawcrate. The banner should have a dog and cat and a separate one with just a cat. We will need a French and English banner. We will provide the French translation once the winner has been selected.

For February our theme is dental health. The banner should have a dog and cat and a separate one with just a cat. We will need a French and English banner. We will provide the French translation once the winner has been selected.

Target Market(s)

pet owners

Industry/Entity Type

Veterinary

Colors

Designer to choose colors to be used in the design.

Requirements
Must have
• dimensions for PCR Banner are: 710px x 280px
Nice to have
• I have attached our logo and some screen shoots of our site so you can get a feel of what it look like. you could also go to www.pawcrate-example.ca and see what the sign in page looks like
Should not have
• images of pet food

```html
<!DOCTYPE html>
<html lang="en">
<head>
<meta charset="utf-8">
<title>PawCrate Winter Contest Banner</title>
<link rel="stylesheet" href="https://fonts.googleapis.com/css2?family=Allura&family=Poppins:wght@300;400;600&display=swap">
<style>
  :root {
    --navy: #1d2a45;
    --pink: #e8276a;
    --black: #151515;
    --white: #ffffff;
    --fur-light: #d9b48a;
    --fur-dark: #8a7a5c;
    --grass: #6f8f4a;
    --dog-light: #e6e0da;
    --dog-dark: #5c5650;
    --brand: #2a2a2a;
  }
  * { margin: 0; padding: 0; box-sizing: border-box; }
  html, body { width: 1200px; height: 473px; overflow: hidden; background: var(--white); }
  .banner { position: relative; width: 1200px; height: 473px; overflow: hidden; }
  .banner-art { position: absolute; inset: 0; width: 1200px; height: 473px; display: block; }
  .headline {
    position: absolute; left: 108px; top: 14px;
    font-family: "Allura", cursive; color: var(--white);
    font-size: 118px; line-height: 1; transform: rotate(-8deg);
  }
  .prize {
    position: absolute; left: 152px; top: 104px;
    font-family: "Allura", cursive; color: var(--white);
    font-size: 62px; line-height: 1; transform: rotate(-6deg);
  }
  .prize .amount { font-size: 40px; vertical-align: 14px; }
  .details {
    position: absolute; left: 110px; top: 218px; width: 580px;
    font-family: "Poppins", sans-serif; font-weight: 300; color: var(--white);
    font-size: 18px; line-height: 24px; text-align: center;
  }
  .brand {
    position: absolute; right: 18px; top: 14px;
    display: flex; align-items: center; gap: 8px;
    font-family: "Poppins", sans-serif; font-weight: 600;
    font-size: 24px; color: var(--brand);
  }
  .brand-mark { width: 16px; height: 16px; background: var(--pink); }
</style>
</head>
<body>
<div class="banner">
  <svg class="banner-art" viewBox="0 0 710 280" preserveAspectRatio="none" aria-hidden="false">
    <defs>
      <linearGradient id="cat-tones" x1="0" y1="0" x2="1" y2="1">
        <stop offset="0" stop-color="var(--grass)"/>
        <stop offset="0.45" stop-color="var(--fur-light)"/>
        <stop offset="1" stop-color="var(--fur-dark)"/>
      </linearGradient>
      <linearGradient id="dog-tones" x1="0" y1="0" x2="1" y2="1">
        <stop offset="0" stop-color="var(--grass)"/>
        <stop offset="0.4" stop-color="var(--dog-light)"/>
        <stop offset="0.8" stop-color="var(--dog-dark)"/>
        <stop offset="1" stop-color="var(--grass)"/>
      </linearGradient>
    </defs>
    <rect class="base-navy" x="0" y="0" width="710" height="280" fill="var(--navy)"/>
    <polygon class="pink-panel" points="115,0 430,0 345,205 0,240 0,62" fill="var(--pink)"/>
    <polygon class="stripe-black" points="430,0 455,0 370,280 345,280 345,205" fill="var(--black)"/>
    <polygon class="stripe-white" points="455,0 468,0 383,280 370,280" fill="var(--white)"/>
    <polygon class="stripe-black" points="468,0 480,0 395,280 383,280" fill="var(--black)"/>
    <polygon class="stripe-white" points="480,0 490,0 405,280 395,280" fill="var(--white)"/>
    <polygon class="stripe-pink" points="490,0 500,0 415,280 405,280" fill="var(--pink)"/>
    <polygon class="stripe-white" points="500,0 710,0 710,280 415,280" fill="var(--white)"/>
    <polygon class="photo-cat" role="img" aria-label="Photo of a ginger kitten on grass"
      points="505,0 710,0 710,42 490,82" fill="url(#cat-tones)"/>
    <polygon class="photo-dog" role="img" aria-label="Photo of a smiling French bulldog with a red collar outdoors"
      points="482,90 710,50 710,280 430,280" fill="url(#dog-tones)"/>
  </svg>

  <div class="headline">Win</div>
  <div class="prize"><span class="amount">$50</span> Gift</div>
  <p class="details">by participating in our chirpbook contest<br>Simply share your pets pics and get a chance to<br>win $50 gift</p>

  <div class="brand"><span class="brand-mark"></span>PawCrate</div>
</div>
</body>
</html>
```